Card design for home renovation company

We are a home renovation company looking for a card design with new logo. We look after every aspect of home renovation from design stage to completion.

Company name is, Harborline Renovations

Target Market(s)

People wanting to have a home designed and built or renovated

Industry/Entity Type

Construction / Home Renovations

Contact Information for Business Card

Company name: Harborline Renovations. Phone, email, website

Font styles to use
Serif
Sans Serif

Colors

Designer to choose only greyscale colors for use in the design.

Requirements
Must have
• Double sided card.
Nice to have
• A roofline logo integrated into the name

```html
<!DOCTYPE html>
<html lang="en">
<head>
<meta charset="utf-8">
<title>Harborline Renovations – Business Card</title>
<link rel="stylesheet" href="https://fonts.googleapis.com/css2?family=Oswald:wght@300;400;600&display=swap">
<style>
  :root {
    --charcoal: #3a3a3a;
    --silver: #9a9a9a;
    --ink: #111111;
    --white: #ffffff;
    --backdrop: #ececec;
    --shadow: rgba(0, 0, 0, 0.22);
  }
  * { margin: 0; padding: 0; box-sizing: border-box; }
  html, body {
    width: 1199px;
    height: 1200px;
    overflow: hidden;
    background: var(--backdrop);
    font-family: "Oswald", sans-serif;
  }
  .canvas { position: relative; width: 1199px; height: 1200px; }
  .card {
    position: absolute;
    left: 142px;
    width: 915px;
    height: 538px;
    background: var(--white);
    box-shadow: 0 4px 10px var(--shadow);
    overflow: hidden;
  }
  .card--front { top: 50px; }
  .card--back { top: 611px; }
  .card__shapes { position: absolute; inset: 0; }
  .holder { position: absolute; left: 62px; top: 143px; color: var(--white); }
  .holder__name { font-weight: 600; font-size: 41px; line-height: 1.08; letter-spacing: 0.3px; }
  .holder__role { font-weight: 300; font-size: 27px; line-height: 1.2; }
  .contacts { position: absolute; left: 62px; top: 284px; list-style: none; color: var(--white); }
  .contacts li {
    display: flex; align-items: center; gap: 16px;
    font-weight: 300; font-size: 27px; line-height: 35.5px;
  }
  .contacts svg { width: 18px; height: 18px; flex: none; }
  .wordmark {
    position: absolute;
    color: var(--ink);
    font-weight: 400;
    line-height: 1.22;
    text-transform: uppercase;
    letter-spacing: 1px;
  }
  .card--front .wordmark { left: 545px; top: 190px; font-size: 56px; }
  .card--back .wordmark { left: 470px; top: 262px; font-size: 60px; }
</style>
</head>
<body>
<main class="canvas">
  <section class="card card--front" aria-label="Card front">
    <svg class="card__shapes" viewBox="0 0 915 538" aria-hidden="true">
      <polygon points="0,0 460,0 460,256 478,238 478,538 0,538" fill="var(--charcoal)"/>
      <polygon points="480,260 502,240 502,538 480,538" fill="var(--silver)"/>
    </svg>
    <div class="holder">
      <p class="holder__name">Dorian Vale Kessler</p>
      <p class="holder__role">Managing Member</p>
    </div>
    <ul class="contacts">
      <li>
        <svg viewBox="0 0 24 24"><path fill="#fff" d="M6.6 10.8a15 15 0 0 0 6.6 6.6l2.2-2.2c.3-.3.7-.4 1-.2 1.1.4 2.3.6 3.6.6.6 0 1 .4 1 1V20c0 .6-.4 1-1 1A17 17 0 0 1 3 4c0-.6.4-1 1-1h3.5c.6 0 1 .4 1 1 0 1.3.2 2.5.6 3.6.1.3 0 .7-.2 1z"/></svg>
        <span>1234 567 890</span>
      </li>
      <li>
        <svg viewBox="0 0 24 24"><rect x="2" y="5" width="20" height="14" fill="#fff"/><path d="M2 5l10 8 10-8" fill="none" stroke="var(--charcoal)" stroke-width="2"/></svg>
        <span>info@harborlinerenovations.com</span>
      </li>
      <li>
        <svg viewBox="0 0 24 24"><path fill="#fff" d="M12 2a6 6 0 0 0-6 6c0 4.5 6 10 6 10s6-5.5 6-10a6 6 0 0 0-6-6zm0 8.5A2.5 2.5 0 1 1 12 5.5a2.5 2.5 0 0 1 0 5z"/><rect x="4" y="20" width="16" height="2" fill="#fff"/></svg>
        <span>www.harborlinerenovations.com</span>
      </li>
    </ul>
    <p class="wordmark">Harborline<br>Renovations</p>
  </section>

  <section class="card card--back" aria-label="Card back">
    <svg class="card__shapes" viewBox="0 0 915 538" aria-hidden="true">
      <rect x="46" y="0" width="30" height="319" fill="var(--silver)"/>
      <rect x="0" y="67" width="796" height="25" fill="var(--charcoal)"/>
    </svg>
    <p class="wordmark">Harborline<br>Renovations</p>
  </section>
</main>
</body>
</html>
```